Werbeflyer/Werbepostkarte für kleines Einzelunternehmen
Hallo Zusammen,
wir sind ein junges Unternehmen, welches überwiegend bayrische Accessoires designen und anfertigen. Unsere Zielgruppe sind sowohl Einzelhändler als auch der Endverbraucher. Insbesondere die feierwütige Gesellschaft der Volksfeste.
Da wir noch recht unbekannt sind, wollen wir durch die Flyer unseren Bekanntheitsgrad steigern und die Flyer auf Volksfesten oder im Einzelhandel verteilen/auslegen lassen.
Aufgabenstellung
Wir stellen uns einen Werbeflyer in Postkartenformat (A6) vor, der beidseitig bedruckt ist. Auf der Vorderseite sollen unsere Produkte so präsentiert werden, dass deutlich wird, was dieses Produkt darstellt und wofür es verwendet werden soll. Dabei beziehe ich mich vor allem auf die "Zwirnel-Ringe", welche zum einen als modisches Accessoires am Handgelenk fundieren und zum anderen als Bierkrug-Markierband. (Produktbilder sind dem Anhang beigefügt)
Zusätzlich soll ein schlichter Schriftzug darauf aufmerksam machen, dass man sich die Zwirnel-Ringe selber generieren/zusammenstellen/designen lassen kann, sodass sie zu jeder Tracht bzw. zu jedem Outfit individuell passen.
Gerne würden wir auch noch die Schlüsselbänder (ein Bild ist ausreichend) mit unterbringen, sodass erkenntlich wird, dass wir nicht nur die Zwirnel-Ringe produzieren, sondern auch andere bayerisch-angehauchte Accessoires.
Zum Schluss soll unser Logo noch mit untergebracht werden.
Die Rückseite soll schlicht gehalten werden und das Layout einer Postkartenrückseite abbilden. Ein Hinweis auf die Firma ( Logo, Adresse, Telefon, E-Mailadresse, Internetadresse) soll ebenfalls abgebildet werden.
Das ganze Design sollte insgesamt sehr schlicht und vintagemäßig von der Farbwahl gehalten werden. Am schönsten wäre es, wenn der Flyer durch sein Design den Zweck einer Postkarte erfüllt und verschickt wird.
Sollten sie noch weitere Materialien, Bilder, etc. benötigen oder noch offene Fragen zu meinen Angaben sind, bitte ich Sie mich einfach zu kontaktieren.
Vielen lieben Dank schonmal im Voraus.

```html
<!DOCTYPE html>
<html lang="de">
<head>
<meta charset="utf-8">
<title>Zwirnelhaus – Postkarte Rückseite</title>
<link rel="stylesheet" href="https://fonts.googleapis.com/css2?family=Open+Sans:wght@300;400&display=swap">
<style>
  :root {
    --paper: #ffffff;
    --edge-band: #f1ede9;
    --frame: #b9b0a9;
    --dash: #c8c1bb;
    --rule: #b3aca7;
    --accent: #e07378;
    --text: #a39992;
  }
  html, body {
    margin: 0;
    padding: 0;
    width: 1200px;
    height: 851px;
    overflow: hidden;
    background: var(--paper);
  }
  .postcard {
    display: block;
    width: 1200px;
    height: 851px;
    font-family: "Open Sans", Arial, sans-serif;
  }
  .edge-band { fill: var(--edge-band); }
  .outer-frame { fill: none; stroke: var(--frame); stroke-width: 2; }
  .writing-area { fill: var(--paper); stroke: var(--dash); stroke-width: 2; stroke-dasharray: 20 14; }
  .stamp-box { fill: none; stroke: var(--dash); stroke-width: 1.6; stroke-dasharray: 22 20; }
  .divider { stroke: var(--accent); stroke-width: 2; }
  .divider-heart { fill: var(--accent); }
  .address-rule { stroke: var(--rule); stroke-width: 1.6; }
  .brand-name { fill: var(--text); font-size: 34px; font-weight: 300; }
  .sender-line { fill: var(--text); font-size: 25px; font-weight: 400; }
</style>
</head>
<body>
<svg class="postcard" viewBox="0 0 1200 851" xmlns="http://www.w3.org/2000/svg">
  <rect class="edge-band" x="0" y="0" width="1200" height="851" role="img" aria-label="Fein gestreifter Randstreifen in hellem Beige"/>
  <rect class="outer-frame" x="1" y="1" width="1198" height="849"/>
  <rect class="writing-area" x="23" y="23" width="1154" height="805"/>

  <text class="brand-name" x="56" y="120">Zwirnelhaus</text>

  <line class="divider" x1="600" y1="58" x2="600" y2="768"/>
  <path class="divider-heart" d="M600 797 C592 788 586 782 586 774 C586 767 591 763 596 763 C598 763 600 765 600 767 C600 765 602 763 604 763 C609 763 614 767 614 774 C614 782 608 788 600 797 Z"/>

  <rect class="stamp-box" x="980" y="57" width="164" height="216"/>

  <line class="address-rule" x1="632" y1="419" x2="1144" y2="419"/>
  <line class="address-rule" x1="632" y1="504" x2="1144" y2="504"/>
  <line class="address-rule" x1="632" y1="589" x2="1144" y2="589"/>
  <line class="address-rule" x1="632" y1="673" x2="1144" y2="673"/>

  <text class="sender-line" x="56" y="682">Lindenweg 12</text>
  <text class="sender-line" x="56" y="720">80997 Beispielstadt</text>
  <text class="sender-line" x="56" y="758">info@zwirnelhaus.example</text>
  <text class="sender-line" x="56" y="795">www.zwirnelhaus.example</text>
</svg>
</body>
</html>
```